stichtinglumo . Eu

With its head office in Amsterdam stichtinglumo.eu we will have offices in the Netherlands, Luxembourg , Belgium, switzerland, Monaco, Liechtenstein and we want pictures of those countries .
UVO.CA a popular Canadian non profit is opening in the Europe and will require a website that appeals those countries we specified.
Please focus on reuse of electronics. Mention ‘WEEE’
Donations to charities, non profit, school and orphanage.
Donates to 3rd world countries like Madagascar
Industry
Technology
Color Preferences
green and blue and similar to uvo.ca
Our Ideas & Additional Information
uvo.ca logo
use these websites as examples to copy and make similar websites
www.bzl.mg
www.uvo.ca
www.tastavorlinka.ba
stichtinglumo.eu - non profit , foundation , association
Target Market(s)
Amsterdam
Industry/Entity Type
Technology, nonprofit
Number of Pages Required
1 page

```html
<!DOCTYPE html>
<html lang="mg">
<head>
<meta charset="utf-8">
<title>BZL – Fanomezana Elektronika</title>
<link href="https://fonts.googleapis.com/css2?family=Poppins:wght@400;500;600;700&display=swap" rel="stylesheet">
<style>
:root{
  --green:#62b862;
  --green-dark:#4ea34e;
  --blue:#0b4fa3;
  --blue-deep:#0a4a9c;
  --ink:#111;
  --text:#333;
  --pale:#ebf2f8;
  --white:#fff;
}
*{margin:0;padding:0;box-sizing:border-box}
html,body{width:1200px;height:3412px;overflow:hidden}
body{font-family:'Poppins',sans-serif;color:var(--ink);background:var(--white);position:relative}
.abs{position:absolute}
.btn{position:absolute;display:flex;align-items:center;justify-content:center;border-radius:22px;color:#fff;font-size:13px;font-weight:600;text-decoration:none}
.btn-green{background:var(--green)}
.btn-blue{background:var(--blue)}

/* header */
.site-header{position:absolute;left:0;top:0;width:1200px;height:95px;background:#fff;z-index:3}
.brand{position:absolute;left:103px;top:10px;width:108px;height:108px;border-radius:50%;background:#fff;box-shadow:0 3px 10px rgba(0,0,0,.12);display:flex;align-items:center;justify-content:center;font-weight:700;font-size:24px;color:var(--green)}
.nav{position:absolute;top:37px;left:290px;display:flex;gap:29px;font-size:13px;color:#222}
.nav-cta{left:910px;top:26px;width:183px;height:42px;font-size:13px}

/* hero */
.hero{position:absolute;left:0;top:95px;width:1200px;height:620px;overflow:hidden}
.hero-photo{position:absolute;inset:0;background:linear-gradient(100deg,#f2f4f5 0%,#e9edf0 35%,#cfd8dc 55%,#9fb8a3 72%,#6f8f6a 85%,#d7dad6 100%)}
.hero-wave{position:absolute;left:0;top:0}
.hero h1{position:absolute;left:105px;top:80px;width:360px;font-size:38px;line-height:50px;font-weight:700}
.hero .lead{position:absolute;left:105px;top:291px;width:380px;font-size:14px;line-height:20px;color:#111}
.badge{position:absolute;top:421px;width:82px;height:82px;border-radius:50%;background:#fff;border:4px solid #e5e8e5;display:flex;align-items:center;justify-content:center}
.badge span{width:58px;height:58px;border-radius:50%;background:var(--green)}
.scroll-cue{position:absolute;left:552px;top:663px;width:96px;height:96px;border-radius:50%;background:#fff;box-shadow:0 6px 18px rgba(0,0,0,.1);display:flex;align-items:center;justify-content:center;z-index:2}

/* steps */
.section-title{position:absolute;left:0;width:1200px;text-align:center;font-size:33px;font-weight:500}
.step{position:absolute;top:861px;width:240px;text-align:center}
.step-ring{width:106px;height:106px;margin:0 auto;border-radius:50%;border:1px solid #ddd;position:relative;display:flex;align-items:center;justify-content:center}
.step-num{position:absolute;left:-2px;top:-2px;width:26px;height:26px;border-radius:50%;background:var(--green);color:#fff;font-size:11px;display:flex;align-items:center;justify-content:center}
.step h3{font-size:14px;font-weight:600;margin-top:16px}
.step p{font-size:12.5px;line-height:18px;color:#333;margin-top:6px}
.step-arrow{position:absolute;top:905px}

/* europe */
.europe{position:absolute;left:0;top:1146px;width:1200px;height:534px;background:var(--pale)}
.europe h2{position:absolute;left:143px;top:122px;font-size:33px;line-height:38px;font-weight:500}
.country{position:absolute;font-size:16px;display:flex;align-items:center;gap:8px}
.map{position:absolute;left:619px;top:92px;width:441px;height:352px;border-radius:16px;background:linear-gradient(135deg,#9fd4e6 0%,#bfe0c4 30%,#cde7c8 60%,#b8dcbc 80%,#9fd3e2 100%)}
.map-card{position:absolute;left:90px;top:177px;width:188px;height:82px;background:#fff;padding:12px 16px}
.map-card b{font-size:16px;font-weight:500}
.map-card p{font-size:11px;line-height:15px;margin-top:6px}

/* stats */
.stat{position:absolute;top:1837px;width:300px;height:300px;border-radius:50%;display:flex;flex-direction:column;align-items:center;justify-content:center;text-align:center}
.stat.outline{border:2px dashed var(--blue)}
.stat.filled{background:var(--green);color:#fff}
.stat strong{font-size:38px;font-weight:700;color:var(--blue)}
.stat.filled strong{color:#fff}
.stat span{font-size:19px;line-height:24px;margin-top:4px}

/* weee */
.weee{position:absolute;left:0;top:2228px;width:1200px;height:536px;background:var(--pale)}
.weee-photo{position:absolute;left:142px;top:92px;width:438px;height:353px;border-radius:14px;background:linear-gradient(135deg,#d9dcdc 0%,#6e6a66 35%,#b88a55 60%,#caa06e 80%,#e3e1dc 100%)}
.weee h2{position:absolute;left:645px;top:115px;width:400px;font-size:36px;line-height:42px;font-weight:500}
.weee p{position:absolute;left:645px;top:250px;width:400px;font-size:13px;line-height:21.5px;color:#333}

/* giving band */
.giving{position:absolute;left:0;top:2764px;width:1200px;height:322px;background:linear-gradient(90deg,#5fae5a,#6cbd62 50%,#5ca85a);color:#fff}
.giving h2{position:absolute;top:78px;font-size:34px;font-weight:500}
.giving p{position:absolute;top:134px;width:430px;font-size:12.5px;line-height:23px}

/* footer */
.site-footer{position:absolute;left:0;top:3086px;width:1200px;height:326px;background:var(--blue-deep);color:#fff}
.footer-brand{position:absolute;left:550px;top:30px;width:100px;text-align:center;font-size:30px;font-weight:700}
.footer-nav{position:absolute;top:150px;left:0;width:1200px;display:flex;justify-content:center;gap:28px;font-size:13px}
.contact{position:absolute;top:186px;display:flex;align-items:center;gap:14px}
.contact-icon{width:42px;height:42px;border-radius:50%;border:1px solid rgba(255,255,255,.6);display:flex;align-items:center;justify-content:center}
.contact small{display:block;font-size:11px;font-weight:600;letter-spacing:.5px}
.contact span{font-size:12.5px}
.footer-rule{position:absolute;left:142px;top:274px;width:916px;height:1px;background:rgba(255,255,255,.25)}
.copyright{position:absolute;left:142px;top:290px;font-size:12px}
.legal{position:absolute;right:142px;top:290px;font-size:12px}
</style>
</head>
<body>

<header class="site-header">
  <div class="brand">BZL</div>
  <nav class="nav"><span>An-trano</span><span>About</span><span>Manomeza</span><span>WEEE Recycling</span><span>Tany</span><span>Fiantraikany</span><span>Contact</span></nav>
  <a class="btn btn-green nav-cta">Manome Electronics</a>
</header>

<section class="hero">
  <div class="hero-photo" role="img" aria-label="Vehivavy mametraka fitaovana elektronika ao anaty harona fanangonana"></div>
  <svg class="hero-wave" width="1200" height="620" viewBox="0 0 1200 620">
    <path d="M0 490 C250 560 420 615 600 615 C780 615 950 560 1200 490 L1200 620 L0 620 Z" fill="#fff"/>
    <path d="M0 490 C250 560 420 615 600 615 C780 615 950 560 1200 490 L1200 540 C950 600 780 625 600 625 C420 625 250 600 0 540 Z" fill="var(--blue)"/>
  </svg>
  <h1>Omeo Fiainana Fanindroany Ny Elektrônikao – Manomeza Anio!</h1>
  <p class="lead">Manohana Sekoly, Asa Fanasoavana &amp; Vondrom piarahamonina Manerana an'i Eoropa &amp; Ambony</p>
  <a class="btn btn-green" style="left:105px;top:354px;width:140px;height:40px">Manome Izao</a>
  <a class="btn btn-blue" style="left:262px;top:354px;width:226px;height:40px">Mianara Momba Ny WEEE</a>
  <div class="badge" style="left:104px"><span></span></div>
  <div class="badge" style="left:194px"><span style="background:#2e7d32"></span></div>
</section>
<div class="scroll-cue">
  <svg width="30" height="42" viewBox="0 0 30 42"><rect x="3" y="3" width="24" height="36" rx="12" fill="none" stroke="var(--green)" stroke-width="2"/><path d="M10 18l5 5 5-5M10 23l5 5 5-5" fill="none" stroke="var(--green)" stroke-width="1.6"/></svg>
</div>

<h2 class="section-title" style="top:790px">Ahoana No Fiasan'ny Fanomezanao</h2>
<div class="step" style="left:185px">
  <div class="step-ring"><span class="step-num">01</span>
    <svg width="50" height="46" viewBox="0 0 50 46" fill="none" stroke="var(--blue)" stroke-width="2"><path d="M10 8h30l-3 34H13z"/><path d="M6 8h38M20 4h10"/><path d="M20 26l5-6 5 6M18 32h14"/></svg>
  </div>
  <h3>Manangona</h3><p>Manomàna famandrihana na fanaterana elektronika any amin'ny biraonay.</p>
</div>
<svg class="step-arrow" style="left:440px" width="24" height="14"><path d="M2 7h19M15 2l6 5-6 5" fill="none" stroke="#aaa" stroke-width="1.4"/></svg>
<div class="step" style="left:480px">
  <div class="step-ring"><span class="step-num">02</span>
    <svg width="50" height="46" viewBox="0 0 50 46" fill="none" stroke="var(--blue)" stroke-width="2"><rect x="4" y="4" width="42" height="28" rx="2"/><path d="M25 32v8M16 42h18M18 14h14l-4-4M32 22H18l4 4"/></svg>
  </div>
  <h3>Fanavaozana</h3><p>Manamboatra sy manao fitiliana fitaovana izahay mba hampiasaina indray.</p>
</div>
<svg class="step-arrow" style="left:736px" width="24" height="14"><path d="M2 7h19M15 2l6 5-6 5" fill="none" stroke="#aaa" stroke-width="1.4"/></svg>
<div class="step" style="left:777px">
  <div class="step-ring"><span class="step-num">03</span>
    <svg width="50" height="46" viewBox="0 0 50 46" fill="none" stroke="var(--blue)" stroke-width="2"><path d="M6 24l19-9 19 9-19 9z M6 24v12l19 9 19-9V24"/><path d="M25 22c-6-4-8-8-4-10 2-1 4 1 4 2 0-1 2-3 4-2 4 2 2 6-4 10z"/><path d="M25 2v4M16 5l2 3M34 5l-2 3"/></svg>
  </div>
  <h3>Manomeza</h3><p>Nalefa tany an-tsekoly, ONG, ary Madagasikara.</p>
</div>

<section class="europe">
  <h2>Manitatra Manerana<br>An'i Eoropa</h2>
  <div class="country" style="left:145px;top:224px"><svg width="12" height="16"><path d="M6 15C2 9 1 7 1 5a5 5 0 0110 0c0 2-1 4-5 10z" fill="var(--green)"/><circle cx="6" cy="5" r="2" fill="#fff"/></svg>Pays-Bas</div>
  <div class="country" style="left:286px;top:224px"><svg width="12" height="16"><path d="M6 15C2 9 1 7 1 5a5 5 0 0110 0c0 2-1 4-5 10z" fill="var(--green)"/><circle cx="6" cy="5" r="2" fill="#fff"/></svg>Luxembourg</div>
  <div class="country" style="left:145px;top:268px"><svg width="12" height="16"><path d="M6 15C2 9 1 7 1 5a5 5 0 0110 0c0 2-1 4-5 10z" fill="var(--green)"/><circle cx="6" cy="5" r="2" fill="#fff"/></svg>Belzika</div>
  <div class="country" style="left:286px;top:268px"><svg width="12" height="16"><path d="M6 15C2 9 1 7 1 5a5 5 0 0110 0c0 2-1 4-5 10z" fill="var(--blue)"/><circle cx="6" cy="5" r="2" fill="#fff"/></svg>Soisa</div>
  <div class="country" style="left:145px;top:313px"><svg width="12" height="16"><path d="M6 15C2 9 1 7 1 5a5 5 0 0110 0c0 2-1 4-5 10z" fill="var(--green)"/><circle cx="6" cy="5" r="2" fill="#fff"/></svg>Monaco</div>
  <div class="country" style="left:286px;top:313px"><svg width="12" height="16"><path d="M6 15C2 9 1 7 1 5a5 5 0 0110 0c0 2-1 4-5 10z" fill="var(--green)"/><circle cx="6" cy="5" r="2" fill="#fff"/></svg>Liechtenstein</div>
  <a class="btn btn-blue" style="left:142px;top:368px;width:183px;height:40px">Mifandraisa Aminay</a>
  <div class="map" role="img" aria-label="Sarintany an'i Eoropa Afovoany misy marika ho an'i Soisa">
    <div class="map-card"><b>Soisa</b><p>123 Ut wisi enim ad minim veniam quis nostrud.</p></div>
  </div>
</section>

<h2 class="section-title" style="top:1760px">Ny Fiantraikantsika Amin'ny Nomery</h2>
<div class="stat outline" style="left:179px"><strong>50000</strong><span>Fitaovana ampiasaina<br>indray</span></div>
<div class="stat outline" style="left:720px"><strong>100</strong><span>Sekoly tohanana</span></div>
<div class="stat filled" style="left:450px"><strong>200</strong><span>Taoniny amin'ny<br>E-Fako Recycle</span></div>

<section class="weee">
  <div class="weee-photo" role="img" aria-label="Olona mitondra boaty misy klavier sy tariby hoavaozina"></div>
  <h2>Responsible Electronics Recycling (WEEE)</h2>
  <p>Ny Stichting LUMO dia manaraka ny fitsipiky ny EU WEEE, izay miantoka ny fanodinana ny fitaovana elektronika rehetra na havaozina araka ny tokony ho izy. Ny fanomezanao dia manampy amin'ny fampihenana ny e-fako ary manohana ny fampandrosoana maharitra.</p>
  <a class="btn btn-blue" style="left:645px;top:377px;width:227px;height:40px">Hamantatra Bebe Kokoa</a>
</section>

<section class="giving" role="img" aria-label="Ankizy ao an-dakilasy mahazo fitaovana, voaloko maitso">
  <h2 style="left:142px">Manome Fitaovana</h2>
  <p style="left:142px">Manaiky solosaina finday, finday, tablette ary maro hafa izahay. Mialà any amin'ny biraonay na mandamina ny fakana.</p>
  <a class="btn btn-blue" style="left:142px;top:196px;width:134px;height:40px">Manome izao</a>
  <h2 style="left:648px">Tohano ara-bola</h2>
  <p style="left:648px">Ny fandraisanao anjara dia manampy anay hanavao ny fitaovana sy hahatratra vondrom-piarahamonina maro kokoa.</p>
  <a class="btn btn-blue" style="left:649px;top:196px;width:134px;height:40px">Manome vola</a>
</section>

<footer class="site-footer">
  <div class="footer-brand">BZL</div>
  <nav class="footer-nav"><span>An-trano</span><span>About</span><span>Manomeza</span><span>WEEE Recycling</span><span>Tany</span><span>Fiantraikany</span><span>Contact</span></nav>
  <div class="contact" style="left:187px">
    <div class="contact-icon"><svg width="18" height="14" fill="none" stroke="#fff" stroke-width="1.5"><rect x="1" y="1" width="16" height="12" rx="1"/><path d="M1 2l8 6 8-6"/></svg></div>
    <div><small>EMAIL</small><span>info@stichtinglumo.eu</span></div>
  </div>
  <div class="contact" style="left:447px">
    <div class="contact-icon"><svg width="14" height="18"><path d="M7 17C2 10 1 8 1 6a6 6 0 0112 0c0 2-1 4-6 11z" fill="#fff"/><circle cx="7" cy="6" r="2.2" fill="var(--blue-deep)"/></svg></div>
    <div><small>ADDRESS</small><span>Stichting LUMO Amsterdam, Netherlands</span></div>
  </div>
  <div class="contact" style="left:824px">
    <div class="contact-icon"><svg width="18" height="18" fill="none" stroke="#fff" stroke-width="1.5"><path d="M4 1l3 4-2 2c1 3 3 5 6 6l2-2 4 3-2 3C8 17 1 10 1 4z"/></svg></div>
    <div><small>TELEFAONINA</small><span>+31 100 200 300</span></div>
  </div>
  <div class="footer-rule"></div>
  <div class="copyright">© 2025 BZL. Zo rehetra voatokana.</div>
  <div class="legal">Politika manokana &nbsp; | &nbsp; Fepetra fampiasana</div>
</footer>

</body>
</html>
```